The Wardrobe Sage needs a business card

The wardrobe sage is a lead generation service serving the Custom Closet industry.

Here is the basic card information:

The Wardrobe Sage
Dorian Pettigrew
Owner/CEO
Charlotte, NC
704-318-5527 Cell
Email: dpettigrew@TheWardrobeSage.com

Additional information for the card:

"High quality, flat rate lead generation exclusively for the custom closet industry"

Bullet points for the back:

- Low fixed cost
- Easy to budget
- Guaranteed qualified Leeds
- Exclusivity per city

Logo attached, head shot attached. Photos of closet systems attached

```html
<!DOCTYPE html>
<html lang="en">
<head>
<meta charset="utf-8">
<title>The Wardrobe Sage – Business Card</title>
<link rel="stylesheet" href="https://fonts.googleapis.com/css2?family=Montserrat:ital,wght@0,400;0,500;0,600;0,700;1,400&display=swap">
<style>
  :root {
    --page: #ececec;
    --card: #ffffff;
    --bronze: #a8652b;
    --ink: #4a4a4a;
    --ink-soft: #555555;
    --panel: rgba(72, 62, 60, 0.88);
    --room-top: #f3ece7;
    --room-wall: #eeddd3;
    --room-floor: #f6f1ec;
    --headshot-a: #3c3f4a;
    --headshot-b: #6f6a66;
  }
  * { box-sizing: border-box; margin: 0; padding: 0; }
  html, body { width: 1200px; height: 1200px; overflow: hidden; }
  body {
    background: var(--page);
    font-family: "Montserrat", sans-serif;
    position: relative;
  }
  .card {
    position: absolute;
    left: 178px;
    width: 844px;
    height: 497px;
    background: var(--card);
    overflow: hidden;
  }
  .card--front { top: 71px; }
  .card--back { top: 640px; height: 495px; }

  /* front */
  .headshot {
    position: absolute;
    left: 78px; top: 120px;
    width: 120px; height: 161px;
    background: linear-gradient(160deg, var(--headshot-b), var(--headshot-a));
  }
  .person { position: absolute; left: 78px; top: 286px; }
  .person__name {
    font-size: 24px; font-weight: 700; letter-spacing: 0.5px;
    color: var(--ink); text-transform: uppercase;
  }
  .person__name span { color: var(--bronze); }
  .person__role { font-size: 20px; color: var(--ink-soft); margin-top: 2px; }

  .brand {
    position: absolute;
    right: 59px; top: 92px;
    display: flex; align-items: center; gap: 12px;
  }
  .brand__mark { width: 14px; height: 14px; border-radius: 50%; background: var(--bronze); }
  .brand__name { font-size: 30px; font-weight: 600; color: var(--bronze); white-space: nowrap; }

  .tagline {
    position: absolute;
    right: 59px; top: 192px;
    text-align: right;
    font-style: italic;
    font-size: 18px; line-height: 24px;
    color: var(--ink-soft);
  }
  .contacts {
    position: absolute;
    right: 52px; top: 346px;
    list-style: none;
  }
  .contacts li {
    display: flex; justify-content: flex-end; align-items: center;
    gap: 14px;
    font-size: 21px; color: var(--ink-soft);
    height: 32px;
  }
  .contacts svg { width: 20px; height: 20px; flex: none; }

  /* back */
  .room {
    position: absolute; inset: 0;
    background:
      linear-gradient(180deg, var(--room-top) 0%, var(--room-wall) 22%, var(--room-wall) 72%, var(--room-floor) 74%, var(--room-floor) 100%);
  }
  .brand-vertical {
    position: absolute;
    left: 168px; top: 60px;
    width: 50px; height: 380px;
    display: flex; align-items: center; justify-content: center;
    writing-mode: vertical-rl;
    transform: rotate(180deg);
  }
  .brand-vertical .brand__name { font-size: 36px; }
  .benefits {
    position: absolute;
    left: 312px; right: 0; top: 98px; height: 300px;
    background: var(--panel);
    list-style: none;
    padding: 66px 79px 0 0;
    text-align: right;
  }
  .benefits li {
    color: #ffffff;
    font-size: 21px; font-weight: 600;
    letter-spacing: 0.4px;
    text-transform: uppercase;
    line-height: 38.5px;
  }
</style>
</head>
<body>

<section class="card card--front">
  <div class="headshot" role="img" aria-label="Headshot of Dorian Pettigrew"></div>
  <div class="person">
    <p class="person__name">Dorian <span>Pettigrew</span></p>
    <p class="person__role">Owner/CEO</p>
  </div>

  <div class="brand">
    <span class="brand__mark"></span>
    <span class="brand__name">The Wardrobe Sage</span>
  </div>

  <p class="tagline">High quality, flat rate lead generation<br>exclusively for the custom closet industry</p>

  <ul class="contacts">
    <li>704-318-5527
      <svg viewBox="0 0 20 20" aria-hidden="true"><rect x="5" y="1.5" width="10" height="17" rx="1.8" fill="none" stroke="var(--bronze)" stroke-width="1.6"/><line x1="8.5" y1="15.5" x2="11.5" y2="15.5" stroke="var(--bronze)" stroke-width="1.4"/></svg>
    </li>
    <li>dpettigrew@TheWardrobeSage.com
      <svg viewBox="0 0 20 20" aria-hidden="true"><rect x="1.5" y="4" width="17" height="12" fill="var(--bronze)"/><path d="M1.5 4 L10 11 L18.5 4" fill="none" stroke="#fff" stroke-width="1.4"/></svg>
    </li>
    <li>Charlotte, NC
      <svg viewBox="0 0 20 20" aria-hidden="true"><path d="M10 2 C6.7 2 4.5 4.4 4.5 7.3 C4.5 11 10 16 10 16 C10 16 15.5 11 15.5 7.3 C15.5 4.4 13.3 2 10 2 Z" fill="none" stroke="var(--bronze)" stroke-width="1.6"/><circle cx="10" cy="7.3" r="2" fill="var(--bronze)"/><ellipse cx="10" cy="17.5" rx="4.5" ry="1.2" fill="none" stroke="var(--bronze)" stroke-width="1.2"/></svg>
    </li>
  </ul>
</section>

<section class="card card--back">
  <div class="room" role="img" aria-label="Faded photo of a custom garage storage and cabinet system"></div>
  <div class="brand-vertical">
    <span class="brand__name">The Wardrobe Sage</span>
  </div>
  <ul class="benefits">
    <li>Low fixed cost</li>
    <li>Easy to budget</li>
    <li>Guaranteed qualified leeds</li>
    <li>Exclusivity per city</li>
  </ul>
</section>

</body>
</html>
```